Film Festival Poster Design Project

The 5th Annual Harwell Open Screen Festival will be taking place on November 12th in Wales at the Larkmoor Cinema, Newport.

It is an all day event and there will be an eclectic mix of films on show.

Target Market(s)

Students 18-25

Industry/Entity Type

Festival

Requirements
Must have
• Title: 5th Harwell Open Screen Festival

Date: Saturday 12th November 2011

Place: Larkmoor Theatre & Cinema, Newport, Wales

Must include the text: BUY TICKETS ONLINE AT WWW.REELGATHERHALL.EXAMPLE

Sponsors & Festival Logo's must be included.
Nice to have
• As the festival is based in Wales, it would be nice to have a slightly Welsh tone to the poster, or a British feel.

```html
<!DOCTYPE html>
<html lang="en">
<head>
<meta charset="utf-8">
<title>5th Harwell Open Screen Festival</title>
<link rel="stylesheet" href="https://fonts.googleapis.com/css2?family=Black+Ops+One&family=Oswald:wght@400&display=swap">
<style>
  :root {
    --teal-light: #6f9f92;
    --teal-mid: #4b7a70;
    --teal-dark: #1c3536;
    --ink: #0e1a1e;
    --cream: #e3efcd;
    --cream-soft: #d4e4bd;
  }
  * { margin: 0; padding: 0; box-sizing: border-box; }
  html, body { width: 1200px; height: 900px; overflow: hidden; background: var(--teal-dark); }
  .poster {
    position: relative;
    width: 1200px;
    height: 900px;
    overflow: hidden;
    background:
      radial-gradient(ellipse 70% 60% at 50% 42%, var(--teal-light) 0%, var(--teal-mid) 50%, var(--teal-dark) 100%);
    font-family: "Black Ops One", "Impact", sans-serif;
    color: var(--ink);
  }
  .tickets {
    position: absolute;
    top: 18px;
    left: 0;
    width: 100%;
    text-align: center;
    font-size: 19px;
    letter-spacing: 0.5px;
    color: var(--ink);
  }
  .emblem {
    position: absolute;
    left: 170px;
    top: 95px;
    width: 860px;
    height: 390px;
    border-radius: 46% 54% 40% 60% / 55% 45% 55% 45%;
    background:
      radial-gradient(ellipse 32% 45% at 48% 48%, #1a2a2c 0%, #1a2a2c 55%, rgba(26,42,44,0) 70%),
      radial-gradient(ellipse 55% 55% at 50% 50%, var(--cream) 0%, var(--cream-soft) 70%, rgba(212,228,189,0) 100%);
  }
  .title {
    position: absolute;
    top: 500px;
    left: 0;
    width: 100%;
    text-align: center;
    line-height: 1;
  }
  .title-top {
    display: block;
    font-size: 58px;
    color: var(--ink);
    letter-spacing: 1px;
  }
  .title-bottom {
    display: block;
    font-size: 78px;
    color: var(--cream);
    letter-spacing: 2px;
    margin-top: 2px;
  }
  .details {
    position: absolute;
    top: 682px;
    left: 0;
    width: 100%;
    text-align: center;
    font-size: 21px;
    white-space: nowrap;
    color: var(--ink);
  }
  .sponsors {
    position: absolute;
    top: 800px;
    left: 190px;
    right: 190px;
    height: 70px;
    display: flex;
    justify-content: space-between;
    align-items: center;
  }
  .sponsor {
    display: flex;
    flex-direction: column;
    align-items: center;
    gap: 6px;
    font-size: 15px;
    color: var(--cream);
    text-align: center;
    line-height: 1.1;
  }
  .sponsor-dot {
    width: 20px;
    height: 20px;
    border-radius: 50%;
    background: var(--cream);
  }
  .sponsor-url { font-size: 9px; }
</style>
</head>
<body>
<main class="poster">
  <p class="tickets">BUY TICKETS ONLINE @ WWW.REELGATHERHALL.EXAMPLE</p>

  <div class="emblem" role="img" aria-label="Welsh dragon rampant in black over a pale cream paint splash"></div>

  <h1 class="title">
    <span class="title-top">5th Harwell Open</span>
    <span class="title-bottom">SCREEN FESTIVAL</span>
  </h1>

  <p class="details">SATURDAY 12TH NOVEMBER 2011 |||| LARKMOOR THEATRE &amp; CINEMA || NEWPORT || WALES</p>

  <footer class="sponsors">
    <div class="sponsor">BRIGHTLANE</div>
    <div class="sponsor">
      <span class="sponsor-dot"></span>
      <span>CINDERHALL</span>
      <span class="sponsor-url">WWW.CINDERHALLFILMS.EXAMPLE</span>
    </div>
    <div class="sponsor">quayside digital media</div>
    <div class="sponsor">HARWELL<br>OPEN SCREEN</div>
    <div class="sponsor">REEL<br>GATHER HALL</div>
  </footer>
</main>
</body>
</html>
```